Infographic for a Life Transformation brand to showcase their principle method

I need a clean infographic which would be used in a brochure to show the 5 steps to achieving a Inner Uprising. (ie Life transformation). I use the theme of a revolution so I would like the graphic to include a raised fist or something to represent a revolution and then the 5 points of information to represent each step.
Needs to very clean and simple. I don't want something that would take up a full page, I want it as a graphic, almost like a big logo. I don't want it laid out like a process chart.

My brand personalities from https://markcharacterhub.com.au/ are
The Everyman and The Magician to give you an idea of my brand.

I've attached my logo so that you can see the colour of it. Graphic doesn't need to match logo but should align with that colour.

Target Market(s)

Top Tier Executives, males, 35-55y old

Industry/Entity Type

Life Coaching

Requirements
Must have
• The graphic must have the 5 Steps: in this order
1.Clarity
2. Measurement
3. Discipline
4. Nutrition
5.Exercise
Nice to have
• It could include these action steps which line up with the 5 steps, It may be too much information by there is the option to include if it works.
1.see it
2. track it
3. do it
4. eat it
5. move it

```html
<!DOCTYPE html>
<html lang="en">
<head>
<meta charset="utf-8">
<title>Inner Uprising – Five Steps</title>
<link rel="stylesheet" href="https://fonts.googleapis.com/css2?family=Roboto:wght@700;900&display=swap">
<style>
  :root {
    --ray-light: #2d63bf;
    --ray-dark: #2254aa;
    --glow: rgba(92, 145, 235, 0.85);
    --navy: #0f3f86;
    --white: #ffffff;
  }
  html, body {
    margin: 0;
    padding: 0;
    overflow: hidden;
  }
  .canvas {
    position: relative;
    width: 1200px;
    height: 793px;
    overflow: hidden;
    background:
      radial-gradient(circle at 50% 50%, var(--glow) 0%, rgba(92, 145, 235, 0.35) 35%, rgba(20, 60, 130, 0) 70%),
      repeating-conic-gradient(from 0deg at 50% 50%, var(--ray-light) 0deg 7.5deg, var(--ray-dark) 7.5deg 15deg);
    font-family: "Roboto", Arial, sans-serif;
  }
  .emblem {
    position: absolute;
    inset: 0;
  }
  .step-label {
    position: absolute;
    margin: 0;
    color: var(--white);
    font-weight: 900;
    font-size: 41px;
    line-height: 1;
    letter-spacing: 0;
    white-space: nowrap;
  }
  .step-1 { left: 486px; top: 292px; }
  .step-2 { left: 502px; top: 341px; }
  .step-3 { left: 490px; top: 390px; }
  .step-4 { left: 465px; top: 436px; }
  .step-5 { left: 463px; top: 483px; }
</style>
</head>
<body>
  <main class="canvas">
    <svg class="emblem" width="1200" height="793" viewBox="0 0 1200 793">
      <g class="step-tabs-outline" fill="none" stroke="#ffffff" stroke-width="10" stroke-linejoin="round">
        <rect x="440" y="283" width="287" height="54" rx="26"/>
        <rect x="440" y="334" width="460" height="50" rx="25"/>
        <rect x="440" y="384" width="374" height="50" rx="25"/>
        <rect x="440" y="432" width="292" height="49" rx="24"/>
        <rect x="440" y="480" width="299" height="52" rx="26"/>
      </g>
      <g class="step-tabs" fill="#0f3f86">
        <rect x="440" y="283" width="287" height="54" rx="26"/>
        <rect x="440" y="334" width="460" height="50" rx="25"/>
        <rect x="440" y="384" width="374" height="50" rx="25"/>
        <rect x="440" y="432" width="292" height="49" rx="24"/>
        <rect x="440" y="480" width="299" height="52" rx="26"/>
      </g>
      <g class="raised-fist" role="img" aria-label="Raised fist symbol of revolution">
        <rect x="326" y="270" width="128" height="266" rx="14" fill="#ffffff"/>
        <rect x="334" y="278" width="112" height="250" rx="10" fill="#0f3f86"/>
        <rect x="340" y="284" width="100" height="238" rx="8" fill="#ffffff"/>
      </g>
    </svg>
    <p class="step-label step-1">1.CLARITY</p>
    <p class="step-label step-2">2. MEASUREMENT</p>
    <p class="step-label step-3">3. DISCIPLINE</p>
    <p class="step-label step-4">4. NUTRITION</p>
    <p class="step-label step-5">5.EXERCISE</p>
  </main>
</body>
</html>
```